Vorlund Business Card Design Needed

We are a consultation firm called "Vorlund Inc" or simply Vorlund. Would would like a simple card utilizing the blue and grays in our logo (perhaps even different shades and hues of blue). Logo and Initials of Card holder one side and information on the other.

Target Market(s)

We are B 2 B company. We deal mostly with upper management.

Industry/Entity Type

Business

Contact Information for Business Card

Name. Title. phone. email. website.

```html
<!DOCTYPE html>
<html lang="en">
<head>
<meta charset="UTF-8">
<title>Vorlund Inc Business Card</title>
<link href="https://fonts.googleapis.com/css2?family=Lato:wght@400;700&display=swap" rel="stylesheet">
<style>
  :root {
    --page-bg: #e9ecef;
    --card-white: #ffffff;
    --card-gray: #e4e4e4;
    --brand-blue: #2e9bd6;
    --brand-blue-deep: #0f8fd0;
    --brand-blue-light: #5cc8ec;
    --ink: #1d1d1d;
    --ink-soft: #555555;
  }
  * { margin: 0; padding: 0; box-sizing: border-box; }
  html, body { width: 1200px; height: 900px; overflow: hidden; }
  body {
    background: var(--page-bg);
    font-family: "Lato", sans-serif;
    position: relative;
  }
  .card {
    position: absolute;
    width: 560px;
    height: 330px;
    border-radius: 22px;
    box-shadow: 0 8px 24px rgba(0,0,0,0.18);
    overflow: hidden;
  }
  /* Front side */
  .card-front {
    left: 70px;
    top: 70px;
    background: linear-gradient(160deg, var(--card-white) 40%, var(--card-gray) 100%);
  }
  .brand-mark {
    position: absolute;
    left: 48px;
    top: 150px;
    display: flex;
    align-items: center;
    gap: 12px;
  }
  .brand-dot {
    width: 24px;
    height: 24px;
    border-radius: 50%;
    background: var(--brand-blue);
  }
  .brand-name {
    font-weight: 700;
    font-size: 25px;
    color: var(--brand-blue);
  }
  .holder {
    position: absolute;
    left: 336px;
    top: 48px;
  }
  .holder-name {
    font-size: 21px;
    color: var(--ink);
  }
  .holder-title {
    font-size: 14px;
    color: var(--ink-soft);
    margin-top: 2px;
  }
  .contact-list {
    position: absolute;
    left: 336px;
    top: 178px;
    list-style: none;
  }
  .contact-list li {
    display: flex;
    align-items: center;
    gap: 10px;
    font-size: 17px;
    color: var(--ink);
    line-height: 27px;
    white-space: nowrap;
  }
  .contact-icon { width: 16px; height: 14px; flex: none; }
  .address {
    position: absolute;
    left: 48px;
    top: 236px;
    font-size: 20px;
    line-height: 27px;
    font-style: normal;
    color: var(--ink);
  }
  .address .postal-code { color: var(--ink-soft); }

  /* Back side */
  .card-back {
    left: 570px;
    top: 500px;
    background: linear-gradient(115deg, var(--brand-blue-deep) 0%, var(--brand-blue-light) 55%, var(--brand-blue-deep) 100%);
  }
  .back-mark {
    position: absolute;
    left: 50%;
    top: 118px;
    transform: translate(-50%, -50%);
    display: flex;
    align-items: center;
    gap: 14px;
  }
  .back-ring {
    width: 34px;
    height: 34px;
    border-radius: 50%;
    border: 4px solid rgba(255,255,255,0.9);
  }
  .back-name {
    font-weight: 700;
    font-size: 40px;
    color: rgba(255,255,255,0.92);
  }
  .back-web {
    position: absolute;
    left: 0;
    right: 0;
    bottom: 58px;
    display: flex;
    align-items: center;
    gap: 10px;
    padding: 0 24px;
  }
  .back-rule {
    flex: 1;
    height: 1.5px;
    background: rgba(255,255,255,0.85);
  }
  .back-url {
    font-size: 19px;
    font-weight: 700;
    color: #ffffff;
  }
</style>
</head>
<body>
  <section class="card card-front" aria-label="Business card front">
    <div class="brand-mark">
      <span class="brand-dot"></span>
      <span class="brand-name">Vorlund Inc</span>
    </div>

    <div class="holder">
      <p class="holder-name">Mark Ellison</p>
      <p class="holder-title">President</p>
    </div>

    <ul class="contact-list">
      <li>
        <svg class="contact-icon" viewBox="0 0 16 14" aria-hidden="true">
          <path d="M1 5 Q8 0 15 5 L13 7 L11 5 L5 5 L3 7 Z" fill="var(--brand-blue)"/>
          <rect x="3" y="7" width="10" height="6" rx="1" fill="var(--brand-blue)"/>
        </svg>
        600-555-0147
      </li>
      <li>
        <svg class="contact-icon" viewBox="0 0 16 14" aria-hidden="true">
          <rect x="1" y="2" width="14" height="10" fill="var(--brand-blue)"/>
          <path d="M1 2 L8 8 L15 2" stroke="#fff" stroke-width="1.2" fill="none"/>
        </svg>
        mail@vorlundinc.com
      </li>
      <li>
        <svg class="contact-icon" viewBox="0 0 16 14" aria-hidden="true">
          <rect x="1" y="1" width="14" height="9" rx="1" fill="none" stroke="var(--brand-blue)" stroke-width="1.6"/>
          <rect x="6" y="11" width="4" height="2" fill="var(--brand-blue)"/>
        </svg>
        www.vorlundinc.com
      </li>
    </ul>

    <address class="address">
      1418 Larkspur Lane<br>
      Brookfield, WI <span class="postal-code">53005-00</span>
    </address>
  </section>

  <section class="card card-back" aria-label="Business card back">
    <div class="back-mark">
      <span class="back-ring"></span>
      <span class="back-name">Vorlund</span>
    </div>
    <div class="back-web">
      <span class="back-rule"></span>
      <span class="back-url">www.vorlundgroup.com</span>
      <span class="back-rule"></span>
    </div>
  </section>
</body>
</html>
```